TECH PROJECT NEEDS NEW SKINS FOR RE-BRANDING

We are a technology project that has a product (crypto wallet) nearing release, have basic designs made so far however we need NEW SKINS/ branding/ design options for this wallet to change the look and feel -- it will be called and re-branded as "KESTRIL" a futuristic/ space/ edgy product so need it to look like so.

YOU ARE ALLOWED TO CHANGE + EXPERIMENT WITH THE LAYOUT/ schema and UI as you see fit -- (we are open to new and creative ideas)

(see WALLET.PNG and PROTFOLIO.PNG ATTACHED --- these are the pages we need new skins for )

(see KESTRIL logo attached --- PLEASE USE THIS LOGO/ VERSIONS OF THIS LOGO IN YOUR DESIGNS/SKIN SUBMISSIONS -- WE PROVIDED THE ai file so feel free to alter the logo a bit to experiment if you want -- we are open and flexible to new creative ideas)

(FOR A MOOD BOARD FOR GUIDANCE on feel/colors/mood-- SEE "SAMPLE INTERFACE 1 & 2" ATTACHED)

Target Market(s)

TECHNOLOGY/SPACE/ FUTURE

Number of Pages Required

2 page

Colors

Designer to choose colors to be used in the design.

Requirements
Must have
• MUST USE OUR KESTRIL LOGO OR A SIMILAR ALTERATION OF IT

```html
<!DOCTYPE html>
<html lang="en">
<head>
<meta charset="utf-8">
<title>KESTRIL — Portfolio</title>
<link href="https://fonts.googleapis.com/css2?family=Roboto+Condensed:wght@400;500;700&display=swap" rel="stylesheet">
<style>
  :root{
    --bg:#0a1412;
    --sidebar:#060c0b;
    --panel:#0c1a17;
    --panel-head:#0e1f1b;
    --line:#16352e;
    --line-soft:#112621;
    --teal:#1fd6a6;
    --teal-dim:#1f6e5a;
    --muted:#3b6f61;
    --text:#e9f2ef;
    --text-soft:#c9d6d2;
    --pink:#e0206e;
    --c-orb:#e08a1e;
    --c-zph:#2452d8;
    --c-aet:#7a25d6;
    --c-lmc:#8b9290;
    --c-tdl:#3f9c94;
    --c-skr:#2b38c9;
  }
  *{box-sizing:border-box;margin:0;padding:0}
  html,body{width:1200px;height:640px;overflow:hidden;background:var(--bg)}
  body{font-family:"Roboto Condensed",Arial Narrow,sans-serif;color:var(--text)}
  .canvas{position:relative;width:1200px;height:640px;overflow:hidden;background:var(--bg)}
  .abs{position:absolute}

  .bracket{
    background:
      linear-gradient(var(--teal),var(--teal)) top left/9px 2px no-repeat,
      linear-gradient(var(--teal),var(--teal)) top left/2px 9px no-repeat,
      linear-gradient(var(--teal),var(--teal)) top right/9px 2px no-repeat,
      linear-gradient(var(--teal),var(--teal)) top right/2px 9px no-repeat,
      linear-gradient(var(--teal),var(--teal)) bottom left/9px 2px no-repeat,
      linear-gradient(var(--teal),var(--teal)) bottom left/2px 9px no-repeat,
      linear-gradient(var(--teal),var(--teal)) bottom right/9px 2px no-repeat,
      linear-gradient(var(--teal),var(--teal)) bottom right/2px 9px no-repeat;
  }

  /* sidebar */
  .sidebar{left:0;top:0;width:62px;height:640px;background:var(--sidebar)}
  .brand{position:absolute;left:0;top:30px;width:62px;display:flex;flex-direction:column;align-items:center;gap:5px}
  .brand-mark{width:12px;height:12px;border:2px solid var(--teal)}
  .brand-name{font-size:10px;font-weight:500;letter-spacing:1px;color:var(--teal)}
  .nav-icon{position:absolute;left:18px;width:26px;height:26px}
  .nav-active{position:absolute;left:4px;top:253px;width:56px;height:40px;background:#0f2a23}

  .plus{position:absolute;width:9px;height:9px}
  .plus::before,.plus::after{content:"";position:absolute;background:var(--teal)}
  .plus::before{left:4px;top:0;width:1px;height:9px}
  .plus::after{left:0;top:4px;width:9px;height:1px}

  .page-title{left:97px;top:36px;font-size:16px;font-weight:700}
  .search{left:374px;top:30px;width:410px;height:27px;border:1px solid var(--line);background:var(--panel);
    border-left:2px solid var(--teal-dim);font-size:10px;color:var(--muted);padding:7px 12px}
  .filter{left:788px;top:30px;width:225px;height:27px;border:1px solid var(--line);background:var(--panel);
    border-right:2px solid var(--teal-dim);font-size:10px;color:var(--muted);padding:7px 12px}
  .add-tx{left:1060px;top:37px;display:flex;align-items:center;gap:6px;font-size:10px;font-weight:500;color:var(--teal)}
  .add-tx .dot{width:15px;height:15px;border-radius:50%;background:var(--teal);color:#062018;font-weight:700;
    font-size:13px;line-height:15px;text-align:center;box-shadow:0 0 8px var(--teal)}

  .tabs{left:97px;top:88px;display:flex;gap:0;font-size:11px;color:var(--muted)}
  .tab{height:28px;line-height:28px;padding:0 7px;margin-right:13px}
  .tab.active{color:var(--text)}

  .est{left:97px;top:138px;width:242px;height:113px;border:1px solid var(--line);background:var(--panel)}
  .est-label{position:absolute;left:1px;top:1px;font-size:7.5px;color:var(--text-soft);border:1px solid var(--teal-dim);padding:2px 4px;background:#0f2520}
  .est-value{position:absolute;left:13px;top:36px;font-size:29px;font-weight:700}
  .est-count{position:absolute;left:13px;top:78px;font-size:14px;color:var(--teal-dim);letter-spacing:.5px}

  .card{width:185px;height:50px;border:1px solid var(--line);background:var(--panel)}
  .card-label{position:absolute;left:12px;top:10px;font-size:7.5px;color:#8aa39c}
  .card-value{position:absolute;left:12px;top:24px;font-size:12px;color:var(--text)}
  .card-value.accent{color:var(--teal);font-size:15px;top:22px}
  .badge{position:absolute;left:118px;top:6px;display:flex;align-items:center;gap:3px;font-size:9.5px;color:var(--teal)}
  .badge i{width:9px;height:9px;border-radius:50%;background:var(--teal);position:relative}
  .badge i::after{content:"";position:absolute;left:2px;top:2px;border:2.5px solid transparent;border-bottom:3px solid #062018;border-top:0}
  .badge.down{color:var(--pink)}
  .badge.down i{background:var(--pink)}
  .badge.down i::after{border-bottom:0;border-top:3px solid #2a0615;top:3px}
  .spark{position:absolute;left:92px;top:14px;width:90px;height:32px}

  .chart{left:804px;top:76px;width:352px;height:175px;border:1px solid var(--line);background:var(--panel)}

  .table{left:97px;top:282px;width:1059px}
  .thead{height:28px;background:var(--panel-head);display:flex;align-items:center;font-size:9px;color:var(--muted);position:relative}
  .th-asset{position:absolute;left:0;top:0;width:156px;height:28px;padding:9px 26px;color:var(--text-soft)}
  .row{position:relative;height:56px;border-bottom:1px solid var(--line-soft);font-size:9.5px;color:var(--text-soft)}
  .row:first-of-type{}
  .row.lead{border-bottom:1px solid var(--teal-dim)}
  .cell{position:absolute;top:0;line-height:56px;white-space:nowrap}
  .coin-dot{position:absolute;left:29px;top:17px;width:22px;height:22px;border-radius:50%;background:#101c1a;border:2px solid var(--dot,#555)}
  .coin-name{left:66px;font-size:11px}
  .chg{display:flex;align-items:center;gap:4px;height:56px;color:var(--pink)}
  .chg i{width:9px;height:9px;border-radius:50%;background:var(--pink);position:relative}
  .chg i::after{content:"";position:absolute;left:2px;top:3px;border:2.5px solid transparent;border-top:3px solid #2a0615;border-bottom:0}
  .chg.up{color:var(--teal)}
  .chg.up i{background:var(--teal)}
  .chg.up i::after{border-top:0;border-bottom:3px solid #062018;top:2px}
  .send{color:#3a4aa8;margin-right:4px}
  .receive{color:var(--teal)}
</style>
</head>
<body>
<div class="canvas">

  <aside class="abs sidebar">
    <div class="brand"><span class="brand-mark"></span><span class="brand-name">KESTRIL</span></div>
    <div class="nav-active bracket"></div>
    <svg class="nav-icon" style="top:164px" viewBox="0 0 26 26" fill="none" stroke="#1f6e5a" stroke-width="1.6"><path d="M4 18a9 9 0 1 1 18 0"/><path d="M13 18l5-6"/></svg>
    <svg class="nav-icon" style="top:208px" viewBox="0 0 26 26" fill="none" stroke="#1f6e5a" stroke-width="1.6"><path d="M4 22h18M7 20v-5M12 20v-8M17 20v-6M5 12l6-5 4 3 6-5"/></svg>
    <svg class="nav-icon" style="top:260px" viewBox="0 0 26 26" fill="none" stroke="#1fd6a6" stroke-width="1.6"><rect x="4" y="8" width="17" height="13" rx="1"/><path d="M6 8l9-4 2 4M16 13h6v4h-6z"/></svg>
    <svg class="nav-icon" style="top:316px" viewBox="0 0 26 26" fill="none" stroke="#1f6e5a" stroke-width="1.6"><path d="M15 3L7 15h6l-2 9 8-12h-6z"/></svg>
    <svg class="nav-icon" style="top:366px" viewBox="0 0 26 26" fill="none" stroke="#1f6e5a" stroke-width="1.6"><path d="M7 19h12a4 4 0 0 0 0-8 6 6 0 0 0-11-1 4.5 4.5 0 0 0-1 9z"/></svg>
  </aside>

  <span class="plus" style="left:74px;top:28px"></span>
  <span class="plus" style="left:74px;top:72px"></span>
  <span class="plus" style="left:74px;top:247px"></span>
  <span class="plus" style="left:353px;top:72px"></span>
  <span class="plus" style="left:353px;top:247px"></span>
  <span class="plus" style="left:781px;top:72px"></span>
  <span class="plus" style="left:781px;top:247px"></span>
  <span class="plus" style="left:1169px;top:28px"></span>
  <span class="plus" style="left:1169px;top:72px"></span>
  <span class="plus" style="left:1169px;top:247px"></span>

  <h1 class="abs page-title">Portfolio</h1>
  <div class="abs search">Search transaction</div>
  <div class="abs filter">All</div>
  <div class="abs add-tx"><span class="dot">+</span>ADD TRANSACTION</div>

  <nav class="abs tabs">
    <span class="tab active bracket">24 H</span>
    <span class="tab">WEEK</span>
    <span class="tab">MONTH</span>
    <span class="tab">YEAR</span>
    <span class="tab">ALL</span>
  </nav>

  <section class="abs est bracket">
    <span class="est-label">EST.ASSETS VALUE</span>
    <div class="est-value">$1,270,000.98</div>
    <div class="est-count">6 ASSETS</div>
  </section>

  <svg width="0" height="0" style="position:absolute">
    <defs>
      <linearGradient id="up-grad" x1="0" x2="1"><stop offset="0" stop-color="#1fd6a6" stop-opacity=".5"/><stop offset="1" stop-color="#1fd6a6"/></linearGradient>
      <linearGradient id="down-grad" x1="0" x2="1"><stop offset="0" stop-color="#e0206e"/><stop offset="1" stop-color="#e0206e" stop-opacity=".5"/></linearGradient>
    </defs>
  </svg>

  <div class="abs card" style="left:375px;top:76px">
    <span class="card-label">PORTFOLIO CHANGE</span><span class="card-value">$1,270,000.98</span>
    <span class="badge"><i></i>36.9%</span>
    <svg class="spark" viewBox="0 0 90 32"><path d="M2 26C14 34 22 18 36 16S56 30 70 20 82 6 88 6" fill="none" stroke="url(#up-grad)" stroke-width="2"/></svg>
  </div>
  <div class="abs card" style="left:375px;top:138px">
    <span class="card-label">PROFIT/LOSS</span><span class="card-value">$1,270,000.98</span>
    <span class="badge"><i></i>36.9%</span>
    <svg class="spark" viewBox="0 0 90 32"><path d="M2 26C14 34 22 18 36 16S56 30 70 20 82 6 88 6" fill="none" stroke="url(#up-grad)" stroke-width="2"/></svg>
  </div>
  <div class="abs card" style="left:375px;top:201px">
    <span class="card-label">24H PROFIT/LOSS</span><span class="card-value">$1,270,000.98</span>
    <span class="badge"><i></i>36.9%</span>
    <svg class="spark" viewBox="0 0 90 32"><path d="M2 26C14 34 22 18 36 16S56 30 70 20 82 6 88 6" fill="none" stroke="url(#up-grad)" stroke-width="2"/></svg>
  </div>
  <div class="abs card" style="left:585px;top:76px">
    <span class="card-label">BEST ASSETS</span><span class="card-value">Stakora - SKR</span>
    <span class="badge"><i></i>36.9%</span>
    <svg class="spark" viewBox="0 0 90 32"><path d="M2 26C14 34 22 18 36 16S56 30 70 20 82 6 88 6" fill="none" stroke="url(#up-grad)" stroke-width="2"/></svg>
  </div>
  <div class="abs card" style="left:585px;top:138px">
    <span class="card-label">WORST ASSETS</span><span class="card-value">Orbcoin - ORB</span>
    <span class="badge down"><i></i>46.5%</span>
    <svg class="spark" viewBox="0 0 90 32"><path d="M2 10C12 2 22 14 36 16S56 4 70 14 82 28 88 28" fill="none" stroke="url(#down-grad)" stroke-width="2"/></svg>
  </div>
  <div class="abs card" style="left:585px;top:201px">
    <span class="card-label">PORTFOLIO AGE</span><span class="card-value accent">6M 24D 3H</span>
  </div>

  <section class="abs chart bracket">
    <svg width="352" height="175" viewBox="0 0 352 175" font-family="Roboto Condensed, sans-serif">
      <defs>
        <linearGradient id="b-orb" x1="0" y1="0" x2="0" y2="1"><stop offset="0" stop-color="#e08a1e" stop-opacity=".75"/><stop offset="1" stop-color="#e08a1e" stop-opacity=".05"/></linearGradient>
        <linearGradient id="b-zph" x1="0" y1="0" x2="0" y2="1"><stop offset="0" stop-color="#2452d8" stop-opacity=".8"/><stop offset="1" stop-color="#2452d8" stop-opacity=".15"/></linearGradient>
        <linearGradient id="b-aet" x1="0" y1="0" x2="0" y2="1"><stop offset="0" stop-color="#7a25d6" stop-opacity=".85"/><stop offset="1" stop-color="#7a25d6" stop-opacity=".15"/></linearGradient>
        <linearGradient id="b-lmc" x1="0" y1="0" x2="0" y2="1"><stop offset="0" stop-color="#8b9290" stop-opacity=".6"/><stop offset="1" stop-color="#8b9290" stop-opacity=".1"/></linearGradient>
        <linearGradient id="b-tdl" x1="0" y1="0" x2="0" y2="1"><stop offset="0" stop-color="#3f9c94" stop-opacity=".7"/><stop offset="1" stop-color="#3f9c94" stop-opacity=".12"/></linearGradient>
        <linearGradient id="b-skr" x1="0" y1="0" x2="0" y2="1"><stop offset="0" stop-color="#2b38c9" stop-opacity=".85"/><stop offset="1" stop-color="#2b38c9" stop-opacity=".15"/></linearGradient>
      </defs>
      <g stroke="#16352e" stroke-width="1">
        <line x1="50" y1="35" x2="338" y2="35"/><line x1="50" y1="78" x2="338" y2="78"/>
        <line x1="50" y1="119" x2="338" y2="119"/><line x1="50" y1="156" x2="338" y2="156"/>
      </g>
      <g fill="#2f5f53" font-size="7" text-anchor="end">
        <text x="46" y="38">60.000</text><text x="46" y="81">40.000</text>
        <text x="46" y="122">20.000</text><text x="46" y="159">0</text>
      </g>
      <rect x="58" y="34" width="37" height="122" fill="url(#b-orb)" stroke="#e08a1e" stroke-opacity=".6"/>
      <rect x="103" y="138" width="37" height="18" fill="url(#b-zph)"/>
      <rect x="149" y="132" width="37" height="24" fill="url(#b-aet)"/>
      <rect x="194" y="138" width="37" height="18" fill="url(#b-lmc)"/>
      <rect x="240" y="129" width="37" height="27" fill="url(#b-tdl)"/>
      <rect x="286" y="138" width="37" height="18" fill="url(#b-skr)"/>
      <g fill="#e9f2ef">
        <circle cx="76.5" cy="9" r="5"/><circle cx="121.5" cy="109" r="5"/><circle cx="167.5" cy="103" r="5"/>
        <circle cx="212.5" cy="109" r="5"/><circle cx="258.5" cy="100" r="5"/><circle cx="304.5" cy="109" r="5"/>
      </g>
      <g fill="#e9f2ef" font-size="7.5" text-anchor="middle">
        <text x="76.5" y="28">61,045.78</text><text x="121.5" y="131">61,045.78</text><text x="167.5" y="125">61,045.78</text>
        <text x="212.5" y="131">61,045.78</text><text x="258.5" y="122">61,045.78</text><text x="304.5" y="131">61,045.78</text>
      </g>
    </svg>
  </section>

  <section class="abs table">
    <div class="thead">
      <span class="th-asset bracket">ASSET NAME</span>
      <span class="abs" style="left:196px">MARKET CAP</span>
      <span class="abs" style="left:284px">VOLUME 24 H</span>
      <span class="abs" style="left:385px">% CHANGE</span>
      <span class="abs" style="left:485px">LAST PRICE</span>
      <span class="abs" style="left:593px">BALANCE</span>
      <span class="abs" style="left:767px">VALUE</span>
      <span class="abs" style="left:884px">PORFOLIO</span>
      <span class="abs" style="left:987px">ACTIONS</span>
    </div>

    <div class="row lead">
      <span class="coin-dot" style="--dot:var(--c-orb)"></span>
      <span class="cell coin-name" style="color:var(--c-orb)">Orbcoin - ORB</span>
      <span class="cell" style="left:196px">120 B</span><span class="cell" style="left:284px">2.7B</span>
      <span class="cell" style="left:389px"><span class="chg"><i></i>46.5%</span></span>
      <span class="cell" style="left:485px">$ 3,664.99</span><span class="cell" style="left:591px">10.00002142 ORB</span>
      <span class="cell" style="left:767px">$ 36,649.98</span><span class="cell" style="left:884px">12,7 %</span>
      <span class="cell" style="left:987px"><span class="send">SEND</span><span class="receive">RECEIVE</span></span>
    </div>
    <div class="row">
      <span class="coin-dot" style="--dot:var(--c-zph)"></span>
      <span class="cell coin-name" style="color:var(--c-zph)">Zephyr - ZPH</span>
      <span class="cell" style="left:196px">30 B</span><span class="cell" style="left:284px">2.7B</span>
      <span class="cell" style="left:389px"><span class="chg"><i></i>22.6%</span></span>
      <span class="cell" style="left:485px">$ 3,664.99</span><span class="cell" style="left:591px">10.00002142 ZPH</span>
      <span class="cell" style="left:767px">$ 36,649.98</span><span class="cell" style="left:884px">12,7 %</span>
      <span class="cell" style="left:987px"><span class="send">SEND</span><span class="receive">RECEIVE</span></span>
    </div>
    <div class="row">
      <span class="coin-dot" style="--dot:var(--c-aet)"></span>
      <span class="cell coin-name" style="color:var(--c-aet)">Aetheron - AET</span>
      <span class="cell" style="left:196px">30 B</span><span class="cell" style="left:284px">2.7B</span>
      <span class="cell" style="left:389px"><span class="chg"><i></i>18.2%</span></span>
      <span class="cell" style="left:485px">$ 3,664.99</span><span class="cell" style="left:591px">10.00002142 AET</span>
      <span class="cell" style="left:767px">$ 36,649.98</span><span class="cell" style="left:884px">12,7 %</span>
      <span class="cell" style="left:987px"><span class="send">SEND</span><span class="receive">RECEIVE</span></span>
    </div>
    <div class="row">
      <span class="coin-dot" style="--dot:var(--c-lmc)"></span>
      <span class="cell coin-name" style="color:var(--c-lmc)">Lumacoin - LMC</span>
      <span class="cell" style="left:196px">30 B</span><span class="cell" style="left:284px">2.7B</span>
      <span class="cell" style="left:389px"><span class="chg"><i></i>10.9%</span></span>
      <span class="cell" style="left:485px">$ 3,664.99</span><span class="cell" style="left:591px">10.00002142 LMC</span>
      <span class="cell" style="left:767px">$ 36,649.98</span><span class="cell" style="left:884px">12,7 %</span>
      <span class="cell" style="left:987px"><span class="send">SEND</span><span class="receive">RECEIVE</span></span>
    </div>
    <div class="row">
      <span class="coin-dot" style="--dot:var(--c-tdl)"></span>
      <span class="cell coin-name" style="color:var(--c-tdl)">Tidal - TDL</span>
      <span class="cell" style="left:196px">30 B</span><span class="cell" style="left:284px">2.7B</span>
      <span class="cell" style="left:389px"><span class="chg"><i></i>10.9%</span></span>
      <span class="cell" style="left:485px">$ 3,664.99</span><span class="cell" style="left:591px">10.00002142 TDL</span>
      <span class="cell" style="left:767px">$ 36,649.98</span><span class="cell" style="left:884px">12,7 %</span>
      <span class="cell" style="left:987px"><span class="send">SEND</span><span class="receive">RECEIVE</span></span>
    </div>
    <div class="row">
      <span class="coin-dot" style="--dot:var(--c-skr)"></span>
      <span class="cell coin-name" style="color:var(--c-skr)">Stakora-SKR</span>
      <span class="cell" style="left:196px">30 B</span><span class="cell" style="left:284px">2.7B</span>
      <span class="cell" style="left:389px"><span class="chg up"><i></i>36.9%</span></span>
      <span class="cell" style="left:485px">$ 3,664.99</span><span class="cell" style="left:591px">10.00002142 SKR</span>
      <span class="cell" style="left:767px">$ 36,649.98</span><span class="cell" style="left:884px">12,7 %</span>
      <span class="cell" style="left:987px"><span class="send">SEND</span><span class="receive">RECEIVE</span></span>
    </div>
  </section>

</div>
</body>
</html>
```